*** Business Card Design Project

I need a logo and business card for my new catering business: "Pomelia". The design should be modern, clean, elegant and refined. One or Two colours only. The design SHOULD NOT include graphics or images. There should be space for my name, phone number and email address (I will provide these to you later).

Industry/Entity Type

Catering

Requirements
Must have
• Must have one or two colours only.
Must include the text "pomelia"
Should not have
• Must not have graphics or images.

```html
<!DOCTYPE html>
<html lang="en">
<head>
<meta charset="utf-8">
<title>Pomelia business card</title>
<link href="https://fonts.googleapis.com/css2?family=Questrial&display=swap" rel="stylesheet">
<style>
  :root {
    --backdrop: #333436;
    --card: #ffffff;
    --ink: #111111;
    --ink-soft: #5e5e5e;
  }
  html, body {
    margin: 0;
    padding: 0;
    width: 1200px;
    height: 1200px;
    overflow: hidden;
    background: var(--backdrop);
    font-family: "Questrial", "Century Gothic", sans-serif;
  }
  .card {
    position: absolute;
    top: 443px;
    width: 521px;
    height: 312px;
    background: var(--card);
    box-shadow: 6px 8px 14px rgba(0, 0, 0, 0.35);
  }
  .card--front { left: 54px; }
  .card--back { left: 625px; }
  .place {
    position: absolute;
    transform: translate(-50%, -50%);
    white-space: nowrap;
    line-height: 1;
  }
  .wordmark {
    left: 50%;
    top: 154px;
    font-size: 31px;
    color: var(--ink);
    letter-spacing: 0.3px;
  }
  .phone {
    top: 265px;
    font-size: 15.5px;
    color: var(--ink-soft);
  }
  .divider-dot {
    top: 263px;
    width: 6px;
    height: 6px;
    border-radius: 50%;
    background: var(--ink);
  }
  .person-name {
    left: 50%;
    top: 98px;
    font-size: 18px;
    color: var(--ink);
  }
  .person-role {
    left: 50%;
    top: 118px;
    font-size: 14.5px;
    color: var(--ink-soft);
  }
  .address-line, .contact-line {
    left: 50%;
    font-size: 15px;
    color: var(--ink-soft);
  }
  .address-line--1 { top: 168px; }
  .address-line--2 { top: 187px; }
  .contact-line { top: 216px; }
  .contact-line .sep { margin: 0 6px; }
</style>
</head>
<body>
  <section class="card card--front">
    <div class="place wordmark">POMELIA</div>
    <span class="place phone" style="left:102px">+63 917 5550142</span>
    <span class="place divider-dot" style="left:200px"></span>
    <span class="place phone" style="left:274px">(083) 555018</span>
    <span class="place divider-dot" style="left:355px"></span>
    <span class="place phone" style="left:432px">(083) 5550276</span>
  </section>

  <section class="card card--back">
    <div class="place person-name">John DOE</div>
    <div class="place person-role">Director</div>
    <div class="place address-line address-line--1">dummy&nbsp; dummy</div>
    <div class="place address-line address-line--2">dummy dummy City dummy</div>
    <div class="place contact-line">john@pomelia.com<span class="sep">|</span>www.pomelia.com</div>
  </section>
</body>
</html>
```